Social Media designs (LinkedIn banner, LinkedIn posts, Instagram)

Hello designers!
We are looking to create some more concepts for our social media identity for a search firm (recruitment company)
I have attached a "brand toolkit" that shows our brand, logo, colour scheme to guide you with regards to colours and identiy.

You will see in the brand toolkit there are some examples of;
- A LinkedIn banner for the company (page 23)
- Social Media posts for LinkedIn and Instagram (page 21)

What we are looking for...

We don't really like the current LinkedIn banner ideas. We would like to see more concepts that look more aesthetically pleasing - the current ideas look quite dull.

We DO like the social media post concepts but we would like to have more templates/options that we can use (similar themes)

We welcome submissions for Social Media designs that we can use with our company branding. Thank you for your work in advance!

```html
<!DOCTYPE html>
<html lang="en">
<head>
<meta charset="utf-8">
<title>Talent knows no borders – banner</title>
<link rel="stylesheet" href="https://fonts.googleapis.com/css2?family=Poppins:wght@500&display=swap">
<style>
  :root {
    --stage: #d9d9d9;
    --forest: #172826;
    --forest-panel: #233430;
    --ring-outer: #2f403c;
    --ring-dark: #5b6966;
    --ring-mid: #8b9592;
    --ring-light: #b9bfbd;
    --photo-spot: #ffffff;
    --headline: #e6e4dc;
  }
  html, body {
    margin: 0;
    width: 1200px;
    height: 1200px;
    overflow: hidden;
    background: var(--stage);
  }
  .banner {
    position: absolute;
    left: 0;
    top: 450px;
    width: 1200px;
    height: 300px;
    display: block;
  }
  .banner__headline {
    font-family: "Poppins", sans-serif;
    font-weight: 500;
    font-size: 104px;
    letter-spacing: -2px;
    fill: var(--headline);
  }
</style>
</head>
<body>
  <svg class="banner" viewBox="0 0 1500 375" xmlns="http://www.w3.org/2000/svg" aria-labelledby="banner-title">
    <title id="banner-title">Talent knows no borders</title>
    <defs>
      <clipPath id="banner-clip"><rect width="1500" height="375"/></clipPath>
      <filter id="ring-shadow" x="-20%" y="-20%" width="140%" height="140%">
        <feDropShadow dx="6" dy="4" stdDeviation="6" flood-color="#000" flood-opacity="0.35"/>
      </filter>
    </defs>
    <g clip-path="url(#banner-clip)">
      <rect class="banner__ground" width="1500" height="375" fill="var(--forest)"/>
      <rect class="banner__side-panel" x="1060" y="0" width="440" height="375" fill="var(--forest-panel)"/>
      <g class="banner__rings" filter="url(#ring-shadow)">
        <circle cx="195" cy="315" r="375" fill="var(--ring-outer)"/>
        <circle cx="195" cy="315" r="325" fill="var(--ring-dark)"/>
        <circle cx="195" cy="315" r="260" fill="var(--ring-mid)"/>
        <circle cx="195" cy="315" r="200" fill="var(--ring-light)"/>
        <circle class="banner__photo-spot" cx="195" cy="315" r="150" fill="var(--photo-spot)"/>
      </g>
      <text class="banner__headline" text-anchor="end">
        <tspan x="1040" y="192">Talent knows</tspan>
        <tspan x="1040" y="278">no borders</tspan>
      </text>
    </g>
  </svg>
</body>
</html>
```